Full re-design of visual identity

We have just re-designed our logo and would like to apply it on our folders, business cards, stationery, and etc... we are attaching new logo + the material we need to re-design... we will provide full corel draw files to help make job easier and also because lot of icons and artwork can be still used...

any doubts we are at your disposal. thanks in advance.

```html
<!DOCTYPE html>
<html lang="en">
<head>
<meta charset="utf-8">
<title>Corvalo Stationery Set</title>
<link rel="stylesheet" href="https://fonts.googleapis.com/css2?family=Josefin+Sans:wght@300;400&display=swap">
<style>
  :root {
    --backdrop: #c4b59a;
    --paper: #ffffff;
    --flap: #fdf1e4;
    --charcoal: #3a3a3c;
    --ink-dark: #111111;
    --name-ink: #5a5a5c;
    --brand-orange: #e8672a;
    --peach: #f6cdb2;
    --light-text: #e6e6e6;
    --muted-text: #8a8a8a;
  }
  * { box-sizing: border-box; margin: 0; padding: 0; }
  html, body { width: 1200px; height: 968px; overflow: hidden; }
  body {
    background: var(--backdrop);
    font-family: "Josefin Sans", sans-serif;
    position: relative;
  }
  .sheet { position: absolute; background: var(--paper); overflow: hidden; }
  .company-name {
    position: absolute;
    font-family: "Josefin Sans", sans-serif;
    font-weight: 400;
    color: var(--name-ink);
    line-height: 1;
    white-space: nowrap;
  }
  .card-back .company-name { color: var(--muted-text); }
  .accent-circle { position: absolute; border-radius: 50%; background: var(--brand-orange); }

  /* Letterhead */
  .letterhead { left: 33px; top: 82px; width: 539px; height: 746px; }
  .letterhead .company-name { left: 17px; top: 16px; font-size: 26px; }
  .letterhead-footer {
    position: absolute; left: 0; top: 678px; width: 412px; height: 53px;
    background: var(--charcoal); color: var(--light-text);
    font-size: 10.5px; font-weight: 300; padding: 15px 0 0 17px; line-height: 14px;
    border-radius: 0 0 26px 0;
  }
  .letterhead-footer .row-one { padding-left: 12px; }
  .letterhead-footer span { margin-right: 18px; }
  .letterhead .accent-circle { left: 418px; top: 634px; width: 96px; height: 96px; }

  /* Envelope */
  .envelope { left: 593px; top: 83px; width: 600px; height: 329px; }
  .envelope-flap { position: absolute; left: 0; top: 0; width: 100%; height: 62px; background: var(--flap); }
  .envelope .company-name { left: 26px; top: 82px; font-size: 24px; }
  .envelope-band {
    position: absolute; left: 0; top: 118px; width: 275px; height: 79px;
    background: var(--charcoal); color: var(--light-text);
    font-size: 10px; font-weight: 300; line-height: 13.5px;
    display: flex; gap: 26px; padding: 5px 0 0 26px;
  }
  .envelope .accent-circle { left: 280px; top: 90px; width: 66px; height: 66px; }

  /* Business card front */
  .card-front { left: 616px; top: 431px; width: 240px; height: 147px; }
  .card-front .company-name { left: 6px; top: 16px; font-size: 30px; }
  .card-front-identity {
    position: absolute; left: 0; top: 94px; width: 150px; text-align: center;
    font-size: 10px; font-weight: 300; color: var(--charcoal); line-height: 13px;
  }
  .card-front .accent-circle { left: 150px; top: 62px; width: 70px; height: 70px; background: var(--peach); }

  /* Business card back */
  .card-back { left: 640px; top: 601px; width: 145px; height: 239px; background: var(--ink-dark); }
  .card-back .company-name { left: 12px; top: 30px; font-size: 22px; }
  .card-back-address {
    position: absolute; left: 34px; top: 111px; font-size: 9.5px; color: var(--muted-text);
    font-weight: 300; line-height: 13.5px;
  }
  .card-back-contact {
    position: absolute; left: 5px; top: 197px; width: 135px; font-size: 9.5px; color: var(--muted-text);
    font-weight: 300; line-height: 11px; text-align: center;
  }

  /* ID badge */
  .id-badge { left: 933px; top: 562px; width: 149px; height: 240px; border-radius: 8px; }
  .id-badge .company-name { left: 29px; top: 12px; font-size: 17px; }
  .id-photo {
    position: absolute; left: 42px; top: 41px; width: 66px; height: 76px;
    background: linear-gradient(180deg, #e8dccd 0%, #c9a98a 55%, #8e7a68 100%);
  }
  .id-name-bar {
    position: absolute; left: 0; top: 119px; width: 100%; height: 19px;
    background: var(--ink-dark); color: #fff; font-size: 10px; text-align: center; line-height: 21px;
  }
  .id-code { position: absolute; left: 0; top: 141px; width: 100%; text-align: center; font-size: 10px; font-weight: 400; color: var(--ink-dark); }
  .id-footer { position: absolute; left: 0; top: 180px; width: 100%; height: 60px; background: var(--brand-orange); }
  .id-badge .accent-circle { left: 96px; top: 160px; width: 38px; height: 38px; border: 3px solid #fff; }
</style>
</head>
<body>

<section class="sheet letterhead" aria-label="Letterhead">
  <div class="company-name">corvalo</div>
  <footer class="letterhead-footer">
    <div class="row-one"><span>Adress line 1</span><span>street name</span><span>city name</span><span>state - zip code</span><span>country</span></div>
    <div><span>Phone:&nbsp; 124 1245 5421</span><span>FAX: 124 1245 5421</span><span>email: name@domain.com</span></div>
  </footer>
  <div class="accent-circle"></div>
</section>

<section class="sheet envelope" aria-label="Envelope">
  <div class="envelope-flap"></div>
  <div class="company-name">corvalo</div>
  <div class="envelope-band">
    <div>Adress line 1<br>street name<br>city name<br>state - zip code<br>country</div>
    <div>Phone:&nbsp; 124 1245 5421<br>FAX: 124 1245 5421<br>email: name@domain.com</div>
  </div>
  <div class="accent-circle"></div>
</section>

<section class="sheet card-front" aria-label="Business card front">
  <div class="company-name">corvalo</div>
  <div class="card-front-identity">Your Name<br>DESIGNATION</div>
  <div class="accent-circle"></div>
</section>

<section class="sheet card-back" aria-label="Business card back">
  <div class="company-name">corvalo</div>
  <div class="card-back-address">Adress line 1<br>street name<br>city name<br>state - zip code<br>country</div>
  <div class="card-back-contact">Phone:&nbsp; 124 1245 5421<br>FAX: 124 1245 5421<br>email: name@domain.com</div>
</section>

<section class="sheet id-badge" aria-label="Employee ID card">
  <div class="company-name">corvalo</div>
  <div class="id-photo" role="img" aria-label="Employee portrait photo"></div>
  <div class="id-name-bar">YOUR NAME</div>
  <div class="id-code">EMP CODE : 00124SA</div>
  <div class="id-footer"></div>
  <div class="accent-circle"></div>
</section>

</body>
</html>
```